Coralvale Meat Traders Business Cards

We require business cards revamped with our logo. A few details we would like to use.

1. Round Edges
2. Our logo over the top of a wagyu cattle background photo on one side of the card

Other side of the card has the below details.

1. Person Name (First & Last)
2. Job Position
3. Mobile Number
4. Email Address
5. Website Address

Simple & Neat.

Target Market(s)

Sales

Industry/Entity Type

Agriculture

Contact Information for Business Card

CORALVALE MEAT TRADERS

Colors

Designer to choose colors to be used in the design.

Requirements
Must have
• Company Logo

```html
<!DOCTYPE html>
<html lang="en">
<head>
<meta charset="utf-8">
<title>Coralvale Meat Traders – Business Cards</title>
<link href="https://fonts.googleapis.com/css2?family=Cinzel:wght@700&family=Montserrat:wght@400;500&family=Tinos&display=swap" rel="stylesheet">
<style>
  :root {
    --maroon: #661422;
    --maroon-soft: #7a2433;
    --faint: #e7d6d9;
    --paper: #ffffff;
    --ink: #2a1a1d;
    --stage: #d9d9db;
  }
  html, body {
    margin: 0;
    padding: 0;
    width: 1200px;
    height: 901px;
    overflow: hidden;
    background: var(--stage);
  }
  .canvas {
    position: relative;
    width: 1200px;
    height: 901px;
  }
  .card {
    position: absolute;
    width: 520px;
    height: 297px;
    border-radius: 22px;
    box-shadow: 0 8px 22px rgba(0,0,0,.25);
    overflow: hidden;
  }
  .card-front {
    left: 60px;
    top: 110px;
    background: var(--maroon);
  }
  .card-back {
    left: 620px;
    top: 494px;
    background: var(--paper);
  }
  .wordmark {
    position: absolute;
    display: flex;
    align-items: center;
    gap: 14px;
    font-family: 'Cinzel', serif;
    font-weight: 700;
    line-height: 1.05;
  }
  .wordmark .mark-dot {
    border-radius: 50%;
    flex: none;
  }
  .wordmark .name-line { display: block; }
  .card-front .wordmark {
    left: 70px;
    top: 100px;
    color: var(--paper);
    font-size: 38px;
  }
  .card-front .mark-dot {
    width: 64px;
    height: 64px;
    border: 0;
    background: var(--paper);
  }
  .card-front .name-line.small { font-size: 20px; letter-spacing: 4px; }
  .watermark-shape {
    position: absolute;
    left: -60px;
    top: 110px;
    width: 300px;
    height: 300px;
    border-radius: 50%;
    background: var(--faint);
  }
  .card-back .wordmark {
    right: 30px;
    top: 30px;
    color: var(--maroon);
    font-size: 24px;
    gap: 10px;
  }
  .card-back .mark-dot {
    width: 40px;
    height: 40px;
    background: var(--maroon);
  }
  .card-back .name-line.small { font-size: 13px; letter-spacing: 2.5px; }
  .person {
    position: absolute;
    right: 30px;
    top: 118px;
    text-align: right;
  }
  .person-name {
    margin: 0;
    font-family: 'Cinzel', serif;
    font-weight: 700;
    font-size: 22px;
    color: var(--maroon);
    letter-spacing: .5px;
  }
  .person-role {
    margin: 2px 0 0;
    font-family: 'Montserrat', sans-serif;
    font-weight: 400;
    font-size: 13px;
    letter-spacing: 1.5px;
    color: var(--ink);
  }
  .contact-list {
    position: absolute;
    right: 30px;
    top: 186px;
    margin: 0;
    padding: 0;
    list-style: none;
    font-family: 'Tinos', serif;
    font-size: 14px;
    color: var(--ink);
  }
  .contact-list li {
    display: flex;
    justify-content: flex-end;
    align-items: center;
    gap: 8px;
    height: 24px;
  }
  .contact-list svg { width: 15px; height: 15px; flex: none; }
</style>
</head>
<body>
<main class="canvas">

  <section class="card card-front" aria-label="Card front">
    <div class="wordmark">
      <span class="mark-dot"></span>
      <span>
        <span class="name-line">Coralvale</span>
        <span class="name-line small">Meat Traders</span>
      </span>
    </div>
  </section>

  <section class="card card-back" aria-label="Card back">
    <div class="watermark-shape"></div>

    <div class="wordmark">
      <span class="mark-dot"></span>
      <span>
        <span class="name-line">Coralvale</span>
        <span class="name-line small">Meat Traders</span>
      </span>
    </div>

    <div class="person">
      <h2 class="person-name">MARCUS HALE</h2>
      <p class="person-role">MANAGING DIRECTOR</p>
    </div>

    <ul class="contact-list">
      <li>047-318 902 654
        <svg viewBox="0 0 16 16" aria-hidden="true"><rect x="4" y="1" width="8" height="14" rx="1.5" fill="none" stroke="var(--maroon)" stroke-width="1.4"/><circle cx="8" cy="12.5" r=".9" fill="var(--maroon)"/></svg>
      </li>
      <li>info@coralvale.com
        <svg viewBox="0 0 16 16" aria-hidden="true"><rect x="1" y="3" width="14" height="10" fill="var(--maroon)"/><path d="M1 3l7 6 7-6" fill="none" stroke="#fff" stroke-width="1.2"/></svg>
      </li>
      <li>www.coralvalemeat.com
        <svg viewBox="0 0 16 16" aria-hidden="true"><circle cx="8" cy="8" r="7" fill="var(--maroon)"/><ellipse cx="8" cy="8" rx="3" ry="7" fill="none" stroke="#fff" stroke-width="1"/><path d="M1 8h14" stroke="#fff" stroke-width="1"/></svg>
      </li>
    </ul>
  </section>

</main>
</body>
</html>
```